Web Design for Meadowfield Turf Crew

Meadowfield Turf Crew needs the photoshop files for a simple, clean and professional web design. I need a home and subpage design, although they can be very similar. See pagestridehub.com for a desired layout, although I'd like to see more design than shown on that site. The goal of the site is to attract both lawn maintenance/landscape customers and build a partner network of consultants that serve the US market. The following are needed:

- home and subpage design
- page: Home, Services, Locations, Consultants, FAQ, Contact
- if subpages have header photo, need to include 5 different header photos for each page
- favicon
Updates

I'll award the design based on the homepage concept. The minor subpage changes and other elements can be worked out in the workroom stage. Thanks, Trent

Industry/Entity Type

It Professional

```html
<!DOCTYPE html>
<html lang="en">
<head>
<meta charset="utf-8">
<title>Meadowfield Turf Crew</title>
<link rel="stylesheet" href="https://fonts.googleapis.com/css2?family=Open+Sans:ital,wght@0,300;0,400;0,600;0,700;1,400&display=swap">
<style>
  :root {
    --green: #5cad47;
    --nav: #4f6275;
    --page: #fafafa;
    --wood-dark: #4a331d;
    --wood-mid: #6a4b2d;
    --text: #2b2b2b;
    --muted: #aab6c0;
    --field: #ebebeb;
    --captcha: #6a6a6a;
    --rule: #d6d8da;
    --photo: #7a9466;
  }
  * { box-sizing: border-box; margin: 0; padding: 0; }
  html, body { width: 1200px; height: 1086px; overflow: hidden; background: var(--page); }
  body { font-family: "Open Sans", sans-serif; color: var(--text); }
  .canvas { position: relative; width: 1200px; height: 1086px; overflow: hidden; background: var(--page); }

  .site-header { position: absolute; left: 0; top: 0; width: 1200px; height: 155px; }
  .brand { position: absolute; left: 169px; top: 63px; display: flex; align-items: center; gap: 10px; }
  .brand-mark { width: 30px; height: 30px; background: var(--green); border-radius: 4px; }
  .brand-name { font-size: 19px; font-weight: 600; color: #6b6b6b; white-space: nowrap; }
  .main-nav { position: absolute; right: 169px; top: 66px; display: flex; gap: 28px; }
  .main-nav a { color: var(--nav); text-decoration: none; font-size: 17px; font-weight: 600; white-space: nowrap; }

  .hero { position: absolute; left: 0; top: 155px; width: 1200px; height: 389px;
    background: linear-gradient(90deg, var(--wood-dark) 0%, var(--wood-mid) 30%, #5a3f24 55%, var(--wood-mid) 80%, var(--wood-dark) 100%); }
  .hero-title { position: absolute; left: 170px; top: 70px; font-size: 35px; line-height: 37.5px; font-weight: 700; color: var(--green); white-space: nowrap; }
  .hero-text { position: absolute; left: 169px; top: 198px; font-size: 17px; line-height: 22.5px; color: #fff; white-space: nowrap; }
  .hero-photo { position: absolute; left: 608px; top: 31px; width: 422px; height: 330px; border: 1px solid #e9e9e9; background: var(--photo); }

  .content { position: absolute; left: 0; top: 544px; width: 1200px; height: 542px;
    background: linear-gradient(180deg, #eef1f2 0%, var(--page) 30%); }
  .intro-title { position: absolute; left: 170px; top: 40px; font-size: 35px; font-weight: 600; color: var(--green); white-space: nowrap; }
  .intro-text { position: absolute; left: 169px; top: 99px; width: 470px; font-size: 13px; line-height: 17px; font-weight: 300; color: #222; }
  .intro-text p + p { margin-top: 17px; }

  .signup-title { position: absolute; left: 700px; top: 38px; width: 350px; text-align: center; font-size: 24px; line-height: 30px; font-weight: 600; color: var(--green); }
  .signup-form { position: absolute; left: 719px; top: 112px; width: 312px; height: 288px; border: 1.5px solid var(--green); border-radius: 13px; }
  .field { position: absolute; left: 13px; width: 284px; height: 34px; background: var(--field); border-radius: 4px;
    font-size: 14px; font-style: italic; color: var(--green); padding: 7px 12px; }
  .captcha { position: absolute; left: 14px; top: 160px; width: 149px; height: 32px; background: var(--captcha);
    color: #fff; font-family: "Courier New", monospace; font-weight: 700; font-size: 20px; letter-spacing: 9px; padding: 2px 9px; }
  .submit { position: absolute; left: 14px; top: 249px; width: 82px; height: 20px; background: var(--green); border-radius: 4px;
    color: #fff; font-size: 12px; font-weight: 700; text-align: center; line-height: 20px; }

  .site-footer { position: absolute; left: 169px; top: 436px; width: 861px; border-top: 1px solid var(--rule); }
  .footer-nav { position: absolute; left: 0; top: 20px; display: flex; gap: 14px; }
  .footer-nav a { color: var(--muted); text-decoration: none; font-size: 14px; }
  .footer-meta { position: absolute; right: 0; top: 20px; text-align: right; color: var(--muted); font-size: 14px; line-height: 22px; }
</style>
</head>
<body>
<div class="canvas">
  <header class="site-header">
    <div class="brand"><span class="brand-mark"></span><span class="brand-name">Meadowfield Turf Crew</span></div>
    <nav class="main-nav">
      <a href="#">Home</a><a href="#">Services</a><a href="#">Locations</a><a href="#">Consultans</a><a href="#">FAQ</a><a href="#">Contact</a>
    </nav>
  </header>

  <section class="hero">
    <h1 class="hero-title">Orem ipsum dolor<br>sit amet, consectetuer<br>adipiscing elit.</h1>
    <p class="hero-text">Lorem ipsum dolor sit amet, consectetuer adipi-<br>scing elit. Maecenas porttitor congue massa. Fusce<br>posuere, magna sed pulvinar ultricies, purus lectus<br>malesuada libero, sit amet commodo magna eros<br>quis urna. Nunc viverra imperdiet enim.</p>
    <div class="hero-photo" role="img" aria-label="Photo of a landscaped courtyard lawn with a reflecting pool and trees"></div>
  </section>

  <main class="content">
    <h2 class="intro-title">Orem ipsum dolor sit amet</h2>
    <div class="intro-text">
      <p>Lorem ipsum dolor sit amet, consectetuer adipiscing elit. Maecenas porttitor congue massa. Fusce posuere, magna sed pulvinar ultricies, purus lectus male-suada libero, sit amet commodo magna eros quis urna. Nunc viverra imperdiet enim.</p>
      <p>Fusce est. Vivamus a tellus. Pellentesque habitant morbi tristique senectus et netus et malesuada fames ac turpis egestas. Proin pharetra nonummy pede. Mauris et orci. Aenean nec lorem. In porttitor. Donec laoreet nonummy augue. Suspendisse dui purus, scelerisque at, vulputate vitae, pretium mattis, nunc. Mauris eget neque at sem venenatis eleifend.</p>
    </div>

    <h2 class="signup-title">Sign up to stay connected with Willow Bend</h2>
    <div class="signup-form">
      <div class="field" style="top:17px">first name...</div>
      <div class="field" style="top:67px">last name...</div>
      <div class="field" style="top:117px">email address...</div>
      <div class="captcha">znqcez</div>
      <div class="field" style="top:200px">Enter word verification in box...</div>
      <div class="submit">submit</div>
    </div>

    <footer class="site-footer">
      <nav class="footer-nav">
        <a href="#">home</a><a href="#">services</a><a href="#">locations</a><a href="#">consultans</a><a href="#">FAQ</a><a href="#">contact</a>
      </nav>
      <div class="footer-meta">@2014 willowbend.co<br>start your page stride hub</div>
    </footer>
  </main>
</div>
</body>
</html>
```